Website for Sports and Exercise Medicine Doctor with active research in stem cells therapies.

I am a sports and exercise medicine doctor with research interests in the cutting edge areas of biological therapies, most notable stem cells. None of my patients are dying of anything, and most of them come to see me to decrease their pain, so they can get back to what they want to do.

The approach i then take is to decrease their pain and support them to achieve the things they wish to achieve. Most people start at "Just make it stop hurting doc" , but I try to move them towards something more important over time.

I would like the website to be very different to other "Doctor or medical websites" in its look. No pictures of doctors in white coats and no pictures of fit old people smiling. I would potentially like the fist thing seen to be a quote:

"Less pain. Everybody wants it, but what are you going to do, once you've got it?"

(But this is only an idea, I am open to anything)

The website will need a couple of things

1. "Locations" I work
2. "Research" I am involved in
3. "Sort Me out" - Clinical information for people to access
4. "Social" - imbedded chirpline and friendgrid
5. "Blog" - imbedded postmill blog
6. "Bio" - the usual bio-stuff

The "Sort Me out" - pages I would like to have the functionality as seen in this site http://www.vandrolix.com.au/platelet/. I intend to put disease topics into these pages (eg Achilles tehdinopathy, osteoarthritis etc etc etc). Once again I am not wedded to this but something along these lines would be good.

To give you an idea these are some sites I like
http://www.harborlantern.com/
http://quimbet.com/
http://orvanstudio.com.sg/
http://milbonhonestkettle.com/
http://www.tessmonthly.com/
http://gravwick.com/#offering
http://pelicanworks.tv/
http://tidalnova.com/
http://foxledger.co.uk/#about

Target Market(s)

20-80 year old.
People with tendon injuries
People with osteoarthritis
People interested in stem cells
I will build the site over time to contain information on multiple sporting injuries and musculoskeletal disorders. It will also become a site for the latest on stem cell research particularly in the area of osteoarthritis.

Industry/Entity Type

Medical

Font styles to use
Sans Serif

Colors
ffffff

Requirements
Nice to have
• To give you an idea these are some sites I like
http://quimbet.com/
http://pelicanworks.tv/
http://tidalnova.com/
Should not have
• Pictures of doctors in white coats or old fit people smiling

```html
<!DOCTYPE html>
<html lang="en">
<head>
<meta charset="utf-8">
<title>Dr Ravel Quint — Sports and Exercise Medicine</title>
<link href="https://fonts.googleapis.com/css2?family=Arimo&family=Ubuntu:wght@300;400;500&display=swap" rel="stylesheet">
<style>
:root{
  --green:#3ab54a;
  --green-text:#3aa845;
  --ink:#333;
  --body:#555;
  --white:#fff;
  --footer:#1f1f1f;
  --hero-a:#e6eef9;
  --hero-b:#3d63c8;
  --hero-c:#0c1f63;
}
*{margin:0;padding:0;box-sizing:border-box}
html,body{width:813px;height:1200px;overflow:hidden;background:var(--white)}
body{font-family:"Ubuntu",sans-serif;color:var(--body);position:relative}
.abs{position:absolute}

/* header */
.site-header{left:0;top:0;width:813px;height:116px;background:var(--white)}
.brand{left:59px;top:12px;width:120px;height:90px;display:flex;flex-direction:column;align-items:center}
.brand-dot{width:54px;height:54px;border-radius:50%;background:var(--green)}
.brand-name{margin-top:6px;font-size:19px;font-weight:400;color:#1d2f6b;white-space:nowrap}
.search{left:578px;top:33px;width:176px;height:24px;border:1px solid #d5d5d5;font-size:10px;color:#888;padding:5px 9px}
.search svg{position:absolute;right:6px;top:6px}
.main-nav{left:285px;top:81px;display:flex;gap:0;font-family:"Arimo",sans-serif;font-size:12px;color:#444}
.main-nav a{color:inherit;text-decoration:none;padding:0 11px;position:relative;height:24px}
.main-nav a.current::after{content:"";position:absolute;left:0;right:0;top:21px;height:3px;background:var(--green)}

/* hero */
.hero{left:0;top:116px;width:813px;height:413px;background:linear-gradient(120deg,var(--hero-a) 0%,#9db5e6 35%,var(--hero-b) 65%,var(--hero-c) 100%)}
.hero-caption{left:113px;top:221px;width:459px;height:43px;background:rgba(80,90,110,.55);color:var(--white);font-size:19px;font-weight:300;padding:11px 13px;letter-spacing:.2px}
.hero-arrow{top:170px;width:42px;height:42px;border-radius:50%;background:rgba(60,60,70,.45);display:flex;align-items:center;justify-content:center}

/* green services band */
.services{left:0;top:529px;width:813px;height:356px;background:var(--green);color:var(--white);text-align:center}
.services h1{position:absolute;left:0;width:813px;top:30px;font-size:19.5px;font-weight:400}
.services .lead{position:absolute;left:50px;width:713px;top:70px;font-size:12.6px;line-height:24px;font-weight:400}
.services .divider{position:absolute;left:170px;width:473px;top:140px;height:2px;background:rgba(0,0,0,.08);box-shadow:0 2px 6px rgba(0,0,0,.12);border-radius:50%}
.service{position:absolute;top:165px;width:200px}
.service svg{display:block;margin:0 auto}
.service h2{margin-top:12px;font-size:14px;font-weight:400;letter-spacing:.3px}
.service p{margin-top:6px;font-size:9.6px;line-height:14.6px;letter-spacing:.4px}
.btn-more{display:inline-block;margin-top:8px;background:var(--white);color:#444;font-size:9.6px;padding:4px 10px;border-radius:1px}

/* content */
.section-title{top:917px;font-size:14px;font-weight:400;color:var(--green-text)}
.photo{background:linear-gradient(135deg,#6aa0e0,#d8e8f8 50%,#3a6ec0)}
.welcome-text{left:185px;top:958px;width:212px;font-size:9.4px;line-height:17px;color:var(--body)}
.welcome-text .caps{text-transform:uppercase;color:#444;margin-bottom:5px}
.blog-photo{background:radial-gradient(circle at 45% 50%,#4a70c8,#0d1a4a 70%)}
.date-badge{left:472px;top:957px;width:36px;height:41px;background:#7dc243;color:var(--white);text-align:center;font-size:10px;line-height:13px;padding-top:3px}
.date-badge b{display:block;font-size:17px;font-weight:400;line-height:19px}
.blog-text{left:603px;top:957px;width:140px;font-size:9.4px;line-height:17px}
.blog-text h3{font-size:11px;font-weight:400;color:#333;margin-bottom:2px}

/* footer */
.site-footer{left:0;top:1130px;width:813px;height:70px;background:var(--footer);color:var(--white);font-size:9.6px}
.footer-links{left:63px;top:17px}
.copyright{left:63px;top:40px}
.social{left:595px;top:23px;display:flex;gap:11px}
.social span{width:24px;height:24px}
</style>
</head>
<body>

<header class="site-header abs">
  <div class="brand abs">
    <div class="brand-dot"></div>
    <div class="brand-name">Dr Ravel Quint</div>
  </div>
  <div class="search abs">Search..
    <svg width="10" height="10" viewBox="0 0 10 10"><circle cx="4" cy="4" r="3" fill="none" stroke="#999" stroke-width="1.4"/><line x1="6.2" y1="6.2" x2="9" y2="9" stroke="#999" stroke-width="1.6"/></svg>
  </div>
  <nav class="main-nav abs">
    <a class="current">HOME</a><a>LOCATIONS</a><a>RESEARCH</a><a>SORT ME OUT</a><a>SOCIAL</a><a>BLOG</a><a>BIO</a>
  </nav>
</header>

<section class="hero abs" role="img" aria-label="Laboratory glassware with test tubes in a rack, blue tones">
  <div class="hero-arrow abs" style="left:58px"><svg width="12" height="20" viewBox="0 0 12 20"><polyline points="10,1 2,10 10,19" fill="none" stroke="#fff" stroke-width="1.5"/></svg></div>
  <div class="hero-arrow abs" style="left:712px"><svg width="12" height="20" viewBox="0 0 12 20"><polyline points="2,1 10,10 2,19" fill="none" stroke="#fff" stroke-width="1.5"/></svg></div>
  <div class="hero-caption abs">LOREM IPSUM DOLOR SIT AMET, CONSECTETUR</div>
</section>

<section class="services abs">
  <h1>HENDRERIT IN VULPUTATE VELIT ESSE MOLESTIE CONSEQUAT</h1>
  <p class="lead">TYPI NON HABENT CLARATEM INSTAM; EST USUS LEGENTIS IN IIS QUI FACIT EORUM CLARITATEM. INVESTIGATIONES DEMONSTRAVERUNT LECTORES LEGERE ME LIUS QUOD II LEGUNT SAEPIUS.</p>
  <div class="divider"></div>

  <div class="service" style="left:63px">
    <svg width="36" height="56" viewBox="0 0 36 56" fill="#fff"><rect x="6" y="0" width="10" height="6"/><rect x="8" y="6" width="8" height="22"/><circle cx="12" cy="34" r="6" fill="none" stroke="#fff" stroke-width="3"/><path d="M20 22a14 14 0 0 1 0 24h-16v-4h16a10 10 0 0 0 0-16z"/><rect x="4" y="48" width="32" height="6"/></svg>
    <h2>RESEARCH</h2>
    <p>Lorem ipsum dolor sit amet adipis msan. Morbi ut elit utipsum tristiquea Pellentesque habitant morbi.</p>
    <span class="btn-more">MORE</span>
  </div>
  <div class="service" style="left:305px">
    <svg width="56" height="56" viewBox="0 0 56 56"><g fill="none" stroke="#fff" stroke-width="3"><path d="M30 10l12 12-6 2-16 24a6 6 0 0 1-9 0l-6-6a6 6 0 0 1 0-9l24-16z"/><circle cx="48" cy="6" r="3.5"/></g><circle cx="22" cy="36" r="3" fill="#fff"/><circle cx="30" cy="30" r="2" fill="#fff"/></svg>
    <h2>SORT ME OUT</h2>
    <p>Lorem ipsum dolor sit amet adipis msan. Morbi ut elit utipsum tristiquea Pellentesque habitant morbi.</p>
    <span class="btn-more">MORE</span>
  </div>
  <div class="service" style="left:546px">
    <svg width="56" height="56" viewBox="0 0 56 56" fill="#fff" stroke="#fff" stroke-width="4"><line x1="42" y1="8" x2="26" y2="30"/><line x1="26" y1="30" x2="8" y2="28"/><line x1="26" y1="30" x2="46" y2="48"/><circle cx="42" cy="8" r="6" stroke="none"/><circle cx="26" cy="30" r="9" stroke="none"/><circle cx="8" cy="28" r="6" stroke="none"/><circle cx="46" cy="48" r="6" stroke="none"/></svg>
    <h2>BIO</h2>
    <p>Lorem ipsum dolor sit amet adipis msan. Morbi ut elit utipsum tristiquea Pellentesque habitant morbi.</p>
    <span class="btn-more">MORE</span>
  </div>
</section>

<h2 class="section-title abs" style="left:59px">WELCOME TO OUR WEBSITE!</h2>
<div class="photo abs" style="left:59px;top:957px;width:111px;height:120px" role="img" aria-label="Hand holding test tubes in a laboratory"></div>
<div class="welcome-text abs">
  <p class="caps">Mes cuml dia sed ineiinias ingoerto lot tes dolore ipsum. Mes cuml dia sed.</p>
  <p>Nemo enim ipsam voluptatem voluiptas Asp aut odit aut fugit sed quia consequuntur nid eos qui rationevoluptatem nesciunt lauenna lingerto otis aliiqt sit amet eism coeismod ict gulate ameti dapibus.</p>
</div>

<h2 class="section-title abs" style="left:461px">BLOG POSTS</h2>
<svg class="abs" style="left:730px;top:917px" width="24" height="14" viewBox="0 0 24 14"><polyline points="7,1 1,7 7,13" fill="none" stroke="#999" stroke-width="1.5"/><polyline points="17,1 23,7 17,13" fill="none" stroke="#999" stroke-width="1.5"/></svg>
<div class="blog-photo abs" style="left:460px;top:957px;width:131px;height:120px" role="img" aria-label="Illustration of glowing neurons in blue"></div>
<div class="date-badge abs"><b>8</b>NOV</div>
<div class="blog-text abs">
  <h3>Lorem ipsum dr sit amet</h3>
  <p>Nemo enim ipsam volm volu iptas sit. Asp aut odigit sedq uia consequuntur magniuirti on evoluptatem nescinusuen nalingerto otis aliiqt sit ame t eismcom. eismod ictgul.</p>
</div>

<footer class="site-footer abs">
  <p class="footer-links abs">Home | Locations | Research | Sort me Out | Social | Blog | Bio</p>
  <p class="copyright abs">Copyrights 2013. All Rights Reserved.</p>
  <div class="social abs">
    <span style="background:#3b5bb0" aria-label="friendgrid"></span>
    <span style="background:#2a8ed8" aria-label="chirpline"></span>
    <span style="background:#f26a1b" aria-label="RSS feed"></span>
    <span style="background:#e0262a" aria-label="Streamvale"></span>
  </div>
</footer>

</body>
</html>
```